Template für Gewinnspiel USB Stick
Zielgruppe
Gewinnspiel-Affine Personen
Aufgabenstellung
Gewünscht ist ein Template für eine Landing-Page eines Gewinnspiels.
Das Thema: Verlosung von 100 USB Sticks 16 GB unter allen Teilnehmern.
Das Layout soll Optisch ansprechend sein. Die Template können nach unten beliebig lang werden. (Inhalte aus der Datenbank)
Benötigte Seiten: Startseite, Datenschutz, Impressum, Gewinnspiel (Formular für das Gewinnspiel) und Teilnahmebedingungen.
Zur Orientierung:
http://brenner.kolbwerk.de/rollbahn
ist eine Seite mit unserem Gewinnspiel.
Klasse wären vielleicht auch Fotos.

```html
<!DOCTYPE html>
<html lang="de">
<head>
<meta charset="utf-8">
<title>USB Gewinnspiel</title>
<link rel="stylesheet" href="https://fonts.googleapis.com/css2?family=Arimo:wght@400;700&family=Roboto+Condensed:ital,wght@0,700;0,900;1,700;1,900&display=swap">
<style>
:root{
  --orange:#f07a12;
  --orange-dark:#c94a06;
  --orange-light:#ffb347;
  --field:#ffc868;
  --ink:#1c1c1c;
  --dark:#141414;
  --white:#ffffff;
  --band:#7a1d08;
}
*{box-sizing:border-box;margin:0;padding:0}
html,body{width:1200px;height:938px;overflow:hidden}
body{
  background:linear-gradient(180deg,#2e2e2e 0,#3a3a3a 130px,var(--band) 142px,#a8320c 180px,var(--band) 225px,#1d0b05 240px,#0c0c0c 938px);
  font-family:Arimo,Arial,sans-serif;position:relative;
}
.page{position:absolute;left:123px;top:42px;width:996px;height:846px;border:5px solid var(--white);border-radius:18px;
  background:linear-gradient(180deg,var(--orange) 0,#e86a0c 40%,#d85a08 100%);overflow:hidden}
.page-title{position:absolute;left:20px;top:14px;font:900 26px "Roboto Condensed",sans-serif;color:var(--white);letter-spacing:.3px}
.hero{position:absolute;left:0;top:52px;width:986px;height:300px;background:linear-gradient(180deg,#1a1a1a,#2a2a2a 70%,#111);}
.hero-swoosh{position:absolute;left:0;top:0}
.hero-product{position:absolute;left:40px;top:40px;width:420px;height:230px;border-radius:16px;
  background:linear-gradient(160deg,#f2f2f2,#b9b9b9 55%,#5b5b5b)}
.hero-photo{position:absolute;left:560px;top:0;width:426px;height:300px;
  background:linear-gradient(90deg,#2a2a2a,#6e5a52 45%,#c9a89a 60%,#2a2020)}
.badge{position:absolute;left:90px;top:120px;width:118px;height:118px;border-radius:50%;background:var(--orange);
  border:4px solid var(--white);color:var(--white);text-align:center;padding-top:18px;box-shadow:0 3px 8px rgba(0,0,0,.4)}
.badge-num{font:900 52px/1 "Roboto Condensed",sans-serif}
.badge-unit{font:700 16px Arimo,sans-serif}
.brand-box{position:absolute;left:327px;top:250px;width:570px;height:86px;border-radius:12px;
  background:linear-gradient(180deg,#3a3a3a,#111);border:2px solid #000;box-shadow:0 4px 10px rgba(0,0,0,.5);
  display:flex;align-items:center;justify-content:center;font:900 62px "Roboto Condensed",sans-serif;color:var(--white);
  text-shadow:0 3px 4px #000}
.nav{position:absolute;top:357px;left:0;width:986px;height:36px}
.nav a{position:absolute;height:36px;border-radius:6px;background:linear-gradient(180deg,#ffb84a,#f07a12);
  border:1px solid #b24a04;color:#4a1a00;font:700 16px "Roboto Condensed",sans-serif;text-decoration:none;
  display:flex;align-items:center;justify-content:center;text-transform:uppercase}
.bullets{position:absolute;left:147px;top:310px}
.bullets span{display:block;width:13px;height:13px;border-radius:3px;background:var(--white);margin-bottom:11px}
.capacity-title{position:absolute;left:50px;top:430px;font:italic 900 22px "Roboto Condensed",sans-serif;color:var(--white)}
.capacity-box{position:absolute;left:20px;top:456px;width:279px;height:120px;border-radius:6px;background:var(--orange-light);border:2px solid #ffd37f}
.cap-icon{position:absolute;top:8px;width:74px;height:74px;border-radius:8px}
.cap-label{position:absolute;top:92px;width:93px;text-align:center;font:700 13px Arimo,sans-serif;color:var(--white);text-shadow:0 1px 1px #8a3a00}
.intro{position:absolute;left:20px;top:590px;width:275px;font:700 12px/1.4 Arimo,sans-serif;color:var(--white)}
.intro p{margin-bottom:13px}
.form-title{position:absolute;left:362px;top:420px;font:italic 900 39px "Roboto Condensed",sans-serif;color:var(--white);text-shadow:2px 2px 3px #7a2a00}
.form-panel{position:absolute;left:322px;top:472px;width:646px;height:254px;border-radius:10px;background:var(--white)}
.form-lead{position:absolute;top:22px;width:100%;text-align:center;font:400 13px Arimo,sans-serif;color:var(--ink)}
.row{position:absolute;left:137px;width:460px;height:22px}
.row label{position:absolute;left:0;top:2px;font:700 13px Arimo,sans-serif;color:var(--ink)}
.field{position:absolute;left:129px;top:0;height:22px;background:var(--field);border:1px solid #e0a240}
.select::after{content:"";position:absolute;right:2px;top:2px;width:16px;height:16px;background:#dfe6f3;border:1px solid #8aa0c8;border-radius:2px}
.select::before{content:"";position:absolute;right:7px;top:9px;border:4px solid transparent;border-top:5px solid #333;z-index:1}
.select span{position:absolute;left:5px;top:1px;font:400 12px Arimo,sans-serif;color:var(--ink)}
.submit{position:absolute;left:211px;top:228px;width:280px;height:46px;border-radius:10px;background:linear-gradient(180deg,#4a4a4a,#0e0e0e);
  border:2px solid #000;color:var(--white);font:900 21px "Roboto Condensed",sans-serif;display:flex;align-items:center;justify-content:center;box-shadow:0 3px 6px rgba(0,0,0,.5)}
.footer{position:absolute;left:0;top:806px;width:986px;height:30px;background:var(--dark);color:#ddd;font:400 12px Arimo,sans-serif;
  display:flex;align-items:center;justify-content:space-between;padding:0 28px}
.footer-tab{position:absolute;left:293px;top:884px;width:380px;height:20px;background:var(--orange);border:4px solid var(--white);border-top:none;border-radius:0 0 18px 18px}
</style>
</head>
<body>
<main class="page">
  <h1 class="page-title">TEILNEHMEN UND EINEN VON 100 STICKS GEWINNEN</h1>

  <section class="hero">
    <svg class="hero-swoosh" width="986" height="300" viewBox="0 0 986 300" aria-hidden="true">
      <path d="M0 20 Q300 60 986 10 L986 40 Q400 90 0 50Z" fill="#e86a0c" opacity=".8"/>
      <path d="M0 230 Q500 300 986 170 L986 300 L0 300Z" fill="#f07a12"/>
    </svg>
    <div class="hero-product" role="img" aria-label="Silberner USB-Stick mit 16 GB"></div>
    <div class="hero-photo" role="img" aria-label="Foto einer jungen Frau mit dunklem Haar"></div>
    <div class="badge"><div class="badge-num">16</div><div class="badge-unit">GigaByte</div></div>
  </section>

  <div class="brand-box">USB GEWINNSPIEL</div>

  <nav class="nav">
    <a href="#" style="left:252px;width:129px">Startseite</a>
    <a href="#" style="left:396px;width:144px">Gewinnspiel</a>
    <a href="#" style="left:558px;width:243px">Teilnahmebedingungen</a>
    <a href="#" style="left:816px;width:150px">Datenschutz</a>
  </nav>

  <div class="bullets" style="left:24px"><span></span><span></span><span></span><span></span><span></span><span></span></div>

  <h2 class="capacity-title">16 GB DATEN PLATZ FÜR</h2>
  <div class="capacity-box">
    <div class="cap-icon" role="img" aria-label="Symbol Musik-CD" style="left:10px;background:linear-gradient(135deg,#333,#000 60%,#3a7fd0)"></div>
    <div class="cap-icon" role="img" aria-label="Symbol Bild" style="left:100px;background:linear-gradient(180deg,#9fd4ff,#4aa0e0 60%,#f6d27a)"></div>
    <div class="cap-icon" role="img" aria-label="Symbol Filmklappe" style="left:190px;background:linear-gradient(180deg,#555,#111)"></div>
    <div class="cap-label" style="left:0">4.500 MP3</div>
    <div class="cap-label" style="left:92px">32.000 Bilder</div>
    <div class="cap-label" style="left:184px">20 Filme</div>
  </div>

  <div class="intro">
    <p>Nehmen Sie heute noch an unserem Gewinnspiel teil und gewinnen Sie einen von 100 HighEnd USB-Sticks der Marke Stormark im Wert von 59,99 Euro.</p>
    <p>Alles was Sie dafür tun müssen, ist das rechte Formular auszufüllen und schon sind Sie bei der Verlosung dabei!</p>
  </div>

  <h2 class="form-title">GEWINNSPIEL-FORMULAR:</h2>
  <form class="form-panel">
    <p class="form-lead">Bitte tragen Sie sich nun für das kostenlose Gewinnspiel ein:</p>
    <div class="row" style="top:73px"><label>Anrede:</label><div class="field select" style="width:63px"><span>—</span></div></div>
    <div class="row" style="top:103px"><label>Vorname:</label><div class="field" style="width:276px"></div></div>
    <div class="row" style="top:133px"><label>Nachname:</label><div class="field" style="width:276px"></div></div>
    <div class="row" style="top:163px"><label>Geburtsdatum:</label>
      <div class="field select" style="width:53px"><span>—</span></div>
      <div class="field select" style="left:189px;width:111px"><span>—</span></div>
      <div class="field select" style="left:314px;width:64px"><span>—</span></div>
    </div>
    <div class="row" style="top:193px"><label>eMail:</label><div class="field" style="width:276px"></div></div>
    <div class="submit">KOSTENLOS TEILNEHMEN!</div>
  </form>

  <footer class="footer">
    <span>AGB &nbsp;•&nbsp; Datenschutz &nbsp;•&nbsp; Impressum</span>
    <span>Webmaster Partnerprogramm</span>
  </footer>
</main>
<div class="footer-tab"></div>
</body>
</html>
```